Bright LumaTrex & Equipments

I need to create full stationery design for the company; Business Card, Envelop, Letterheads, Calendar and email template.

Our company is specialized in the import and export of nutritional, pharmaceutical and cosmetics in addition to medical equipments.

These is no limitation on how to use colors within the design.

Target Market(s)

Global

Industry/Entity Type

Healthcare

Other font styles liked:
• a font close to logo. Letterhead body text to be different than the address text

Requirements
Nice to have
• We will have multiple locations so it is good to keep space for future addresses.
• Stationary requirements:
• Letterhead: A4
• Envelopes: 3 regular sizes : large, medium and small (i do not know the sizes)
• Colors: extracted from the logo

```html
<!DOCTYPE html>
<html lang="en">
<head>
<meta charset="utf-8">
<title>Bright LumaTrex &amp; Equipments – Stationery</title>
<link href="https://fonts.googleapis.com/css2?family=Nunito:wght@800&family=Arimo:wght@400;700&display=swap" rel="stylesheet">
<style>
  :root {
    --sky: #29a9e1;
    --navy: #14166b;
    --paper: #ffffff;
    --backdrop: #ececee;
    --ink: #3a3a3a;
    --edge: #dcdde0;
  }
  * { box-sizing: border-box; margin: 0; padding: 0; }
  html, body { width: 1200px; height: 937px; overflow: hidden; }
  body {
    position: relative;
    background: var(--backdrop);
    font-family: "Arimo", Arial, sans-serif;
    color: var(--ink);
  }
  address { font-style: normal; }
  .sheet {
    position: absolute;
    background: var(--paper);
    border: 1px solid var(--edge);
    overflow: hidden;
  }
  /* Plain footer band: navy rule above a sky band */
  .band {
    position: absolute; left: 0; right: 0; bottom: 0;
    background: var(--sky);
    box-shadow: 0 -4px 0 var(--paper), 0 -8px 0 var(--navy);
  }
  .brand { display: flex; align-items: center; gap: 6px; }
  .brand-mark { background: var(--sky); flex: none; }
  .brand-name {
    font-family: "Nunito", "Varela Round", sans-serif;
    font-weight: 800;
    color: var(--sky);
    line-height: 1.05;
  }
  .web {
    position: absolute;
    color: #fff;
    font-family: "Arimo", Arial, sans-serif;
    letter-spacing: 0.22em;
  }

  /* Letterhead */
  .letterhead { left: 185px; top: 66px; width: 388px; height: 546px; }
  .letterhead .brand { position: absolute; left: 18px; top: 28px; }
  .letterhead .brand-mark { width: 20px; height: 20px; }
  .letterhead .brand-name { font-size: 14px; width: 130px; }
  .letterhead .contact {
    position: absolute; right: 18px; top: 24px;
    font-size: 4.6px; line-height: 7.2px; text-align: right;
  }
  .letterhead .contact strong { font-weight: 700; }
  .letter-body {
    position: absolute; left: 36px; top: 140px; width: 300px;
    font-size: 5px; line-height: 7.3px;
  }
  .letter-body p { margin-bottom: 7px; }
  .letter-body .gap { margin-bottom: 18px; }
  .signature-area { width: 30px; height: 14px; background: #e7e7ea; margin: 2px 0 6px; }
  .letterhead .band { height: 52px; }

  /* Folder */
  .folder { left: 636px; top: 40px; width: 458px; height: 576px; }
  .folder .brand {
    position: absolute; left: 0; right: 0; top: 230px;
    flex-direction: column; gap: 14px; text-align: center;
  }
  .folder .brand-mark { width: 64px; height: 64px; }
  .folder .brand-name { font-size: 40px; width: 360px; }
  .folder .band { height: 62px; }
  .folder .web { left: 18px; bottom: 10px; font-size: 10px; }

  /* Business cards */
  .card-front { left: 45px; top: 655px; width: 177px; height: 104px; border-radius: 6px; }
  .card-front .brand { position: absolute; left: 9px; top: 14px; gap: 4px; }
  .card-front .brand-mark { width: 9px; height: 9px; }
  .card-front .brand-name { font-size: 8px; width: 70px; }
  .card-front .person {
    position: absolute; left: 103px; top: 16px; font-size: 4.2px; line-height: 5.6px;
  }
  .card-front .person strong { font-size: 5px; display: block; }
  .card-front .band { height: 24px; box-shadow: 0 -2px 0 var(--paper), 0 -4px 0 var(--navy); }
  .card-front .address {
    position: absolute; left: 8px; bottom: 6px; font-size: 4px; line-height: 5.4px; color: #fff;
  }
  .card-back { left: 45px; top: 782px; width: 177px; height: 102px; border-radius: 6px; }
  .card-back .brand { position: absolute; left: 0; right: 0; top: 28px; flex-direction: column; gap: 4px; }
  .card-back .brand-mark { width: 14px; height: 14px; }
  .card-back .brand-name { font-size: 10px; text-align: center; width: 130px; }

  /* Envelope front */
  .envelope { left: 265px; top: 671px; width: 433px; height: 209px; }
  .envelope .brand { position: absolute; left: 15px; top: 22px; }
  .envelope .brand-mark { width: 24px; height: 24px; }
  .envelope .brand-name { font-size: 18px; width: 150px; }
  .envelope .band { height: 44px; }
  .envelope .web { left: 13px; bottom: 8px; font-size: 9px; }

  /* Envelope back */
  .envelope-back { left: 737px; top: 671px; width: 432px; height: 209px; }
  .envelope-back .flap {
    position: absolute; left: 0; top: 0; width: 100%; height: 72px;
    background: var(--sky); border-radius: 0 0 34px 34px;
  }
  .envelope-back .web { left: 0; right: 0; top: 28px; text-align: center; font-size: 11.5px; }
</style>
</head>
<body>

<section class="sheet letterhead" aria-label="Letterhead">
  <div class="brand">
    <span class="brand-mark"></span>
    <span class="brand-name">Bright LumaTrex &amp; Equipments</span>
  </div>
  <address class="contact">
    <strong>1204 Harbor Tower</strong><br>
    <strong>Lakeside Road UAE</strong><br>
    012 345 6789<br>
    012 345 6789<br>
    012 345 6789<br>
    info@brightlumatrex.com<br>
    www.brightlumatrex.com
  </address>
  <div class="letter-body">
    <p>July 2, 2012</p>
    <p><strong>Dear Cili,</strong><br>ABC Building, def St., Country Name</p>
    <p class="gap">is simply dummy text of the printing and typesetting industry. Lorem Ipsum has been the industry's standard dummy text ever since the 1500s, when an unknown printer took a galley of type and scrambled it to make a type specimen book. It has survived not only five centuries, but also the leap into electronic typesetting, remaining essentially unchanged. It was popularised in the 1960s with the release of Letraset sheets containing Lorem Ipsum passages, and more recently with desktop publishing software like Aldus PageMaker including versions of Lorem Ipsum.</p>
    <p class="gap">is simply dummy text of the printing and typesetting industry. Lorem Ipsum has been the industry's standard dummy text ever since the 1500s, when an unknown printer took a galley of type and scrambled it to make</p>
    <p>is simply dummy text of the printing and typesetting industry. Lorem Ipsum has been the industry's standard dummy text ever since the 1500s, when an unknown printer took a galley of type and scrambled it to make a type specimen book. It has survived not only five centuries, but also the leap into electronic typesetting, remaining essentially unchanged. It was popularised in the 1960s with the release of Letraset sheets containing Lorem Ipsum passages, and more recently with desktop publishing software like Aldus PageMaker including versions of Lorem Ipsum.</p>
    <p>Best Regards,</p>
    <div class="signature-area" role="img" aria-label="Handwritten signature"></div>
    <p><strong>Daniel Reyes</strong><br>Director<br><br>ABC Building, def St., Country Name</p>
  </div>
  <div class="band"></div>
</section>

<section class="sheet folder" aria-label="Presentation folder">
  <div class="brand">
    <span class="brand-mark"></span>
    <span class="brand-name">Bright LumaTrex &amp; Equipments</span>
  </div>
  <div class="band"></div>
  <span class="web">www.brightlumatrex.com</span>
</section>

<section class="sheet card-front" aria-label="Business card front">
  <div class="brand">
    <span class="brand-mark"></span>
    <span class="brand-name">Bright LumaTrex &amp; Equipments</span>
  </div>
  <div class="person">
    <strong>OMAR HADLEY</strong>
    Managing Director<br><br>
    &#9742; 012 345 6789<br>
    &#9742; 012 345 6789<br>
    &#9742; 012 345 6789<br>
    info@brightlumatrex.com<br>
    www.brightlumatrex.com
  </div>
  <div class="band"></div>
  <address class="address">1204 Harbor Tower<br>Lakeside Road UAE</address>
</section>

<section class="sheet card-back" aria-label="Business card back">
  <div class="brand">
    <span class="brand-mark"></span>
    <span class="brand-name">Bright LumaTrex &amp; Equipments</span>
  </div>
</section>

<section class="sheet envelope" aria-label="Envelope front">
  <div class="brand">
    <span class="brand-mark"></span>
    <span class="brand-name">Bright LumaTrex &amp; Equipments</span>
  </div>
  <div class="band"></div>
  <span class="web">www.brightlumatrex.com</span>
</section>

<section class="sheet envelope-back" aria-label="Envelope back">
  <div class="flap"></div>
  <span class="web">www.brightlumatrex.com</span>
</section>

</body>
</html>
```